依頼詳細
ロゴマークは既に決定しているので、このロゴマークを使用したデザインをお願いします。法律関係の仕事ですので、堅く、シンプルでかつ信頼感と重厚感のあるデザインを希望します。弊社のイメージカラーの落ち着いたブルーをベースにしてほしいです。表裏のデザインで、裏はごくシンプルな感じでイメージしていますが、基本的なイメージは踏襲していただいてデザインは感性におまかせしたいと思います。
納品時は、記載項目詳細記載のあるものと、役職以下を空白にしたものでお願いします。
記載項目
ロゴ:添付参照
住所1:〒890−0612 鹿児島県鹿児島市桜見台4番27号 青嵐ビル7階 TEL 099-314-5926 FAX 099-314-5927
住所2:〒108−0094 東京都港区白帆台5−17−8楓葉ビル4階
TEL 03-4281-9350 FAX 099-4281-9351
マーク:QKV5, データ守秘マーク 添付参照
役職:代表
氏名:杉森 晴也
よみがな:SUGIMORI HARUYA
携帯電話番号:090−4158−6092
メールアドレス:(空白でお願いします)
ホームページアドレス:(空白でお願いします)

希望イメージ
シンプル 複雑
単色 カラフル
暗い 明るい
日常 高級
遊び心 厳粛
未来的 伝統的
女性的 男性的
希望する色
青系
納品ファイル
• 高解像度JPG (.jpg)
• イラストレーター形式 (.ai)
• PNG形式 (.png)
補足説明

```html
<!DOCTYPE html>
<html lang="ja">
<head>
<meta charset="utf-8">
<title>Minato Link 名刺</title>
<link rel="stylesheet" href="https://fonts.googleapis.com/css2?family=Noto+Serif+JP:wght@400;600;700&display=swap">
<style>
  :root {
    --stage: #a9abae;
    --paper: #ffffff;
    --navy: #14317a;
    --navy-deep: #071a5c;
    --royal: #1c3ea8;
    --ink: #1a1a1a;
    --mist: #cfdcf2;
    --badge: #4d74b8;
  }
  * { margin: 0; padding: 0; box-sizing: border-box; }
  html, body { width: 856px; height: 1200px; overflow: hidden; background: var(--stage); }
  body { position: relative; font-family: "Noto Serif JP", serif; color: var(--ink); }

  .card { position: absolute; left: 57px; width: 765px; height: 520px; overflow: hidden; }
  .card--front { top: 43px; background: var(--paper); }
  .card--back {
    top: 634px;
    background: radial-gradient(ellipse at 25% 15%, #2f5fd0 0%, var(--royal) 35%, var(--navy-deep) 100%);
  }

  .wave-art { position: absolute; right: 0; top: 0; width: 430px; height: 100%; }
  .back-wave { position: absolute; left: 0; top: 0; width: 100%; height: 100%; }

  .brand { position: absolute; display: flex; align-items: center; gap: 14px; }
  .brand__mark { width: 30px; height: 30px; background: currentColor; }
  .brand__name { font-size: 40px; font-weight: 600; letter-spacing: 0.5px; line-height: 1; }
  .card--front .brand { left: 80px; top: 118px; color: var(--navy); }
  .card--back .brand { left: 50%; top: 50%; transform: translate(-50%, -50%); color: #fff; }
  .card--back .brand__name { font-size: 52px; }
  .card--back .brand__mark { width: 40px; height: 40px; }

  .person { position: absolute; left: 80px; top: 248px; }
  .person__role { font-size: 15px; margin-bottom: 6px; }
  .person__name { font-size: 34px; font-weight: 600; letter-spacing: 6px; display: inline-block; }
  .person__roman { font-size: 12px; margin-left: 18px; vertical-align: middle; }

  .contact { position: absolute; left: 80px; top: 358px; }
  .contact__firm { font-size: 17px; font-weight: 700; margin-bottom: 8px; }
  .contact__line { font-size: 12.5px; line-height: 18.5px; white-space: nowrap; }

  .badges { position: absolute; left: 508px; top: 432px; display: flex; gap: 46px; }
  .badge { width: 78px; height: 78px; border-radius: 50%; background: var(--badge); opacity: 0.85; }
  .badge--seal { border-radius: 10px; }
</style>
</head>
<body>
  <section class="card card--front">
    <svg class="wave-art" viewBox="0 0 430 520" role="img" aria-label="淡いブルーの流線装飾">
      <defs>
        <linearGradient id="mistFade" x1="0" y1="0" x2="1" y2="0">
          <stop offset="0" stop-color="#ffffff" stop-opacity="0"/>
          <stop offset="0.6" stop-color="#dfe8f7"/>
          <stop offset="1" stop-color="#c3d4ef"/>
        </linearGradient>
      </defs>
      <rect width="430" height="520" fill="url(#mistFade)"/>
    </svg>

    <div class="brand">
      <span class="brand__mark"></span>
      <span class="brand__name">Minato Link</span>
    </div>

    <div class="person">
      <p class="person__role">代表</p>
      <p><span class="person__name">杉森 晴也</span><span class="person__roman">Sugimori Haruya</span></p>
    </div>

    <div class="contact">
      <p class="contact__firm">社会保険労務士法人 ミナトリンク</p>
      <p class="contact__line">〒890−0612　鹿児島県鹿児島市桜見台4番27号　青嵐ビル7階</p>
      <p class="contact__line">TEL 099-314-5926　FAX 099-314-5927</p>
      <p class="contact__line">〒108−0094　東京都港区白帆台5−17−8楓葉ビル4階</p>
      <p class="contact__line">TEL 03-4281-9350　FAX 099-4281-9351</p>
      <p class="contact__line">Mobile 090−4158−6092　E-mail xxxxx@xxxxx</p>
      <p class="contact__line">Web http://www.xxxxx.xxxxx</p>
    </div>

    <div class="badges">
      <span class="badge" aria-label="データ守秘マーク"></span>
      <span class="badge" aria-label="QKV5"></span>
    </div>
  </section>

  <section class="card card--back">
    <svg class="back-wave" viewBox="0 0 765 520" role="img" aria-label="明るいブルーの流線装飾">
      <defs>
        <radialGradient id="glow" cx="0.2" cy="0.1" r="0.6">
          <stop offset="0" stop-color="#6f95ea" stop-opacity="0.45"/>
          <stop offset="1" stop-color="#2f5fd0" stop-opacity="0"/>
        </radialGradient>
      </defs>
      <rect width="765" height="520" fill="url(#glow)"/>
    </svg>
    <div class="brand">
      <span class="brand__mark"></span>
      <span class="brand__name">Minato Link</span>
    </div>
  </section>
</body>
</html>
```